Marrowfield Transport Company Business Card Design

We are a company that delivers natural saltwater (from the ocean) to aquarium companies, restaurants and home marine tanks. I would like a new business card to suit.

Must include Name, company name, abn, contact number and website as well as logo (see attached).

Looking for a design that stands out, has a clean but unique appearance.

Double and single sided entries welcome

• Logo

```html
<!DOCTYPE html>
<html lang="en">
<head>
<meta charset="utf-8">
<title>Marrowfield Transport Company – Business Card</title>
<link rel="stylesheet" href="https://fonts.googleapis.com/css2?family=PT+Sans:ital,wght@0,400;0,700;1,700&display=swap">
<style>
  :root {
    --backdrop: #2b2b2b;
    --card-front: #4752a3;
    --card-back: #ffffff;
    --ocean-deep: #0b83c6;
    --ocean-light: #6dc8e8;
    --ocean-pale: #a9e0f4;
    --ink: #3a3a3a;
    --white: #ffffff;
  }
  * { margin: 0; padding: 0; box-sizing: border-box; }
  html, body { width: 1200px; height: 900px; overflow: hidden; }
  body {
    background: var(--backdrop);
    font-family: "PT Sans", "Myriad Pro", Arial, sans-serif;
    position: relative;
  }
  .card {
    position: absolute;
    top: 308px;
    width: 514px;
    height: 285px;
    border-radius: 22px;
    overflow: hidden;
  }
  .card--front { left: 72px; background: var(--card-front); }
  .card--back { left: 615px; background: var(--card-back); }

  .brand {
    position: absolute;
    text-align: center;
    font-weight: 700;
    line-height: 1.05;
  }
  .brand small { display: block; font-weight: 700; }
  .card--front .brand {
    left: 0; right: 0; top: 118px;
    color: var(--white);
    font-size: 42px;
  }
  .card--front .brand small { font-size: 18px; margin-top: 4px; }
  .front-web {
    position: absolute;
    left: 0; right: 0; top: 250px;
    text-align: center;
    color: var(--ocean-light);
    font-size: 15px;
  }

  .card--back .brand {
    left: 40px; top: 60px;
    width: 232px;
    color: var(--ocean-deep);
    font-size: 36px;
  }
  .card--back .brand small { font-size: 17px; margin-top: 3px; }
  .holder-name {
    position: absolute;
    right: 29px; top: 72px;
    color: var(--ocean-deep);
    font-size: 19px;
    font-weight: 700;
    font-style: italic;
  }
  .contact-list {
    position: absolute;
    left: 55px; top: 152px;
    list-style: none;
    color: var(--ink);
    font-size: 13.5px;
    line-height: 18px;
  }
  .contact-list li { display: flex; align-items: center; gap: 5px; }
  .contact-list svg { width: 10px; height: 10px; fill: var(--ocean-deep); }
  .wave-band {
    position: absolute;
    left: 0; right: 0; bottom: 0;
    height: 58px;
    background: linear-gradient(180deg, var(--ocean-pale), var(--ocean-light));
  }
  .abn {
    position: absolute;
    left: 55px; top: 238px;
    color: var(--white);
    font-size: 11px;
  }
</style>
</head>
<body>

<section class="card card--front" aria-label="Card front">
  <p class="brand">Marrowfield<small>Transport Company</small></p>
  <p class="front-web">www.marrowfieldtransport.com.au</p>
</section>

<section class="card card--back" aria-label="Card back">
  <div class="wave-band" role="img" aria-label="Ocean wave splash illustration"></div>
  <p class="brand">Marrowfield<small>Transport Company</small></p>
  <p class="holder-name">Owen Harlow</p>
  <ul class="contact-list">
    <li><svg viewBox="0 0 10 10"><rect x="2" y="0" width="6" height="10" rx="1"/></svg>0491-570-118</li>
    <li><svg viewBox="0 0 10 10"><circle cx="5" cy="5" r="5"/></svg>www.marrowfieldtransport.com.au</li>
    <li><svg viewBox="0 0 10 10"><rect x="0" y="2" width="10" height="7"/></svg>hello@marrowfieldtransport.com.au</li>
  </ul>
  <p class="abn">ABN:12 345 678 901</p>
</section>

</body>
</html>
```